Copper Lantern Haulage

We are a 3PL freight brokerage company looking to create a website to attract new customers. Some ideas on how other freight websites look is located at these links, https://www.bluefinchcarriers.example/services, https://marlowcargo.example/freight-brokerage/.
We would like to have a quote feature implemented into this website.

We specialize in heavy-haul, specialized loads, flatbed, and dry vans.

```html
<!DOCTYPE html>
<html lang="en">
<head>
<meta charset="utf-8">
<title>Copper Lantern Haulage</title>
<link href="https://fonts.googleapis.com/css2?family=Montserrat:wght@500;600;700;800&family=Open+Sans:wght@400;600&display=swap" rel="stylesheet">
<style>
:root{
  --red:#a50d0d;
  --ink:#1a1a1a;
  --body:#555;
  --light:#f4f4f6;
  --grey:#e6e6e6;
  --navy:#0b0b24;
  --white:#fff;
}
*{margin:0;padding:0;box-sizing:border-box}
html,body{width:1200px;height:3282px;overflow:hidden}
body{position:relative;background:var(--white);font-family:"Open Sans",sans-serif;color:var(--ink)}
.abs{position:absolute}
.section{position:absolute;left:0;width:1200px;overflow:hidden}
.heading{font-family:"Montserrat",sans-serif;font-weight:500;font-size:28px;line-height:36px;color:var(--ink)}
.label{font-family:"Montserrat",sans-serif;font-weight:500;font-size:12px;color:var(--red);text-transform:uppercase}
.para{font-size:13.5px;line-height:22px;color:var(--body)}
.btn{position:absolute;background:var(--red);color:var(--white);font-family:"Montserrat",sans-serif;font-weight:700;font-size:13.5px;letter-spacing:1.2px;display:flex;align-items:center;justify-content:center;box-shadow:0 8px 18px rgba(165,13,13,.3)}
.photo{position:absolute}

/* hero */
.hero{top:0;height:596px;background:var(--light)}
.hero-road{left:0;top:0;width:1200px;height:596px;clip-path:polygon(382px 0,1200px 0,1200px 596px);background:linear-gradient(160deg,#6f7a55 0%,#8a8670 35%,#5d5b58 70%,#474544 100%)}
.hero-truck{left:620px;top:160px;width:540px;height:350px;border-radius:18px 60px 10px 10px;background:linear-gradient(100deg,#d1232a 0%,#b8161c 38%,#2a2748 40%,#1d1b38 100%)}
.brand{left:143px;top:70px;font-family:"Montserrat",sans-serif;font-weight:800;font-size:19px;line-height:22px;color:var(--red);display:flex;align-items:center;gap:8px}
.brand i{width:14px;height:14px;background:var(--red);display:block}
.nav a{position:absolute;white-space:nowrap;top:0;text-decoration:none;color:var(--white);font-family:"Montserrat",sans-serif;font-weight:600;font-size:13px}
.nav-cta{left:904px;top:15px;width:141px;height:46px;border:1.5px solid var(--white);color:var(--white);font-family:"Montserrat",sans-serif;font-weight:600;font-size:13px;letter-spacing:1px;display:flex;align-items:center;justify-content:center}
.tagline{left:154px;top:203px;font-family:"Montserrat",sans-serif;font-weight:500;font-size:11.5px;color:var(--red)}
.hero-title{left:154px;top:232px;font-family:"Montserrat",sans-serif;font-weight:500;font-size:37px;line-height:44px;color:var(--ink);white-space:nowrap}
.hero-title b{color:var(--red);font-weight:700}
.hero-text{left:154px;top:336px;width:400px}

/* services */
.services{top:596px;height:522px;background:var(--white)}
.service{position:absolute;width:210px}
.service .icon{width:54px;height:50px;position:relative}
.service .icon::before{content:"";position:absolute;left:0;top:10px;width:40px;height:40px;border-radius:50%;background:#f6dede}
.service svg{position:relative}
.service h3{font-family:"Montserrat",sans-serif;font-weight:500;font-size:16px;margin-top:14px;color:var(--ink)}
.service p{font-size:13px;line-height:21px;color:var(--body);margin-top:12px}

/* about */
.about{top:1118px;height:512px;background:var(--grey)}
.about-photo{left:0;top:0;width:575px;height:512px;background:linear-gradient(180deg,#c9c6bd 0%,#b0aea6 55%,#6b675f 75%,#55524c 100%)}
.about-truck{left:0;top:85px;width:662px;height:305px;border-radius:8px 40px 20px 20px;background:linear-gradient(90deg,#f1f1f1 0%,#e2e2e2 38%,#d4232a 42%,#b81a1f 100%)}

/* team */
.team{top:1630px;height:523px;background:var(--white)}
.card{position:absolute;top:198px;width:204px;height:195px;background:var(--white);box-shadow:0 6px 20px rgba(0,0,0,.08);text-align:center}
.avatar{position:absolute;left:64px;top:-38px;width:76px;height:76px;border-radius:50%;border:3px solid var(--white);background:linear-gradient(180deg,#d9d6d2,#a6a19a);box-shadow:0 3px 10px rgba(0,0,0,.15)}
.card h4{margin-top:64px;font-family:"Montserrat",sans-serif;font-weight:500;font-size:16px;color:var(--ink)}
.card p{margin:10px auto 0;width:168px;font-size:11px;line-height:18px;color:#666}
.socials{display:flex;justify-content:center;gap:30px;margin-top:16px}
.socials span{width:9px;height:9px;border-radius:50%;background:var(--red)}
.arrow{position:absolute;width:32px;height:39px;display:flex;align-items:center;justify-content:center;background:var(--white)}
.dots{left:565px;display:flex;gap:19px}
.dots span{width:12px;height:12px;border-radius:50%;border:1.5px solid var(--white)}
.dots span.on{background:var(--white)}

/* stats */
.stats{top:2153px;height:159px;background:var(--white)}
.stat{position:absolute;top:46px;width:220px;margin-left:-110px;text-align:center}
.stat strong{display:block;font-family:"Montserrat",sans-serif;font-weight:700;font-size:28px;color:var(--red)}
.stat span{display:block;margin-top:12px;font-family:"Montserrat",sans-serif;font-weight:500;font-size:14px;color:#333}

/* quote */
.quote{top:2312px;height:603px;background:var(--grey)}
.quote-truck{left:0;top:96px;width:548px;height:332px;border-radius:10px 50px 30px 20px;background:linear-gradient(90deg,#e8e8e8 0%,#d9d9d9 26%,#d4232a 30%,#b1171c 100%)}
.field-label{position:absolute;left:611px;font-family:"Montserrat",sans-serif;font-weight:600;font-size:11.5px;color:#333}
.field{position:absolute;left:611px;width:434px;border:1px solid #b9b9b9;background:#ececec;font-family:"Montserrat",sans-serif;font-size:12px;color:#888;padding:0 22px;display:flex;align-items:center}
.field.area{align-items:flex-start;padding-top:12px}

/* footer */
.footer{top:2915px;height:367px;background:var(--navy);color:var(--white)}
.foot-brand{left:147px;top:88px;font-family:"Montserrat",sans-serif;font-weight:800;font-size:24px;line-height:28px;color:var(--white);display:flex;align-items:center;gap:10px}
.foot-brand i{width:18px;height:18px;background:var(--white);display:block}
.foot-text{left:157px;top:160px;width:220px;font-size:13px;line-height:20px;color:#e4e4ea}
.foot-col h5{font-family:"Montserrat",sans-serif;font-weight:600;font-size:16px;margin-bottom:18px}
.foot-col li{list-style:none;font-size:13px;line-height:28px;color:#e4e4ea}
.ring{width:32px;height:32px;border-radius:50%;border:1.5px solid var(--white)}
.rule{left:0;top:305px;width:1200px;height:1px;background:#2a2a45}
.copy{top:330px;font-size:11px;color:#e4e4ea}
</style>
</head>
<body>

<!-- HERO -->
<section class="section hero">
  <div class="photo hero-road" role="img" aria-label="Winding mountain road with a motorcyclist"></div>
  <div class="photo hero-truck" role="img" aria-label="Red semi truck with navy curtain trailer"></div>
  <div class="abs brand"><i></i>COPPER LANTERN<br>HAULAGE</div>
  <nav class="abs nav" style="left:0;top:30px">
    <a style="left:558px">HOME</a>
    <a style="left:632px">ABOUT US</a>
    <a style="left:732px">SERVICE</a>
    <a style="left:820px">DRIVERS</a>
  </nav>
  <div class="abs nav-cta">GET A QUOTE</div>
  <div class="abs tagline">⟶ TRANSPORTATION,ROAD TRUCKING, LOGISTICS.</div>
  <h1 class="abs hero-title">WE PROVIDE <b>BEST</b><br><b>TRANSPORT</b> SERVICE!</h1>
  <p class="abs para hero-text">Lorem ipsum dolor sit amet, consectetur adipiscing elit, sed do eiusmod tempor incididunt ut labore et dolore magna aliqua. Quis ipsum suspendisse ultrices.</p>
  <div class="btn" style="left:154px;top:429px;width:140px;height:44px">LEARN MORE</div>
</section>

<!-- SERVICES -->
<section class="section services">
  <div class="abs label" style="left:152px;top:86px">LET'S KNOW OUR SERVICES?</div>
  <h2 class="abs heading" style="left:154px;top:116px">Let’s Know About What We<br>Provide For Customars.</h2>
  <p class="abs para" style="left:154px;top:211px;width:375px">Lorem ipsum dolor sit amet, consectetur adipiscing elit, sed do eiusmod tempor incididunt ut labore et dolore magna aliqua Quis ipsum suspendiss.</p>
  <p class="abs para" style="left:154px;top:300px;width:375px">Lorem ipsum dolor sit amet, consectetur adipiscing elit, sed do eiusmod tempor incididunt.</p>
  <div class="btn" style="left:154px;top:379px;width:140px;height:44px">LEARN MORE</div>

  <div class="service" style="left:599px;top:79px">
    <div class="icon"><svg width="54" height="50" viewBox="0 0 54 50" fill="none" stroke="#a50d0d" stroke-width="2"><rect x="14" y="16" width="22" height="16"/><path d="M36 22h8l6 6v4H36z"/><circle cx="20" cy="38" r="4"/><circle cx="44" cy="38" r="4"/><path d="M18 10h14"/></svg></div>
    <h3>HEAVY-HAUL</h3>
    <p>Lorem ipsum dolor sit amet, cons ectetur adipiscing elit, sed do eiu dmod fdsg tempor.</p>
  </div>
  <div class="service" style="left:832px;top:79px">
    <div class="icon"><svg width="54" height="50" viewBox="0 0 54 50" fill="none" stroke="#a50d0d" stroke-width="2"><path d="M8 30h34M8 26v4"/><path d="M42 22h6l4 6v4H42z"/><circle cx="16" cy="38" r="4"/><circle cx="46" cy="38" r="4"/><rect x="14" y="18" width="20" height="8"/></svg></div>
    <h3>FLATBED</h3>
    <p>Lorem ipsum dolor sit amet, cons ectetur adipiscing elit, sed do eiu dmod fdsg tempor.</p>
  </div>
  <div class="service" style="left:599px;top:275px">
    <div class="icon"><svg width="54" height="50" viewBox="0 0 54 50" fill="none" stroke="#a50d0d" stroke-width="2"><path d="M30 6l14 8v16l-14 8-14-8V14z"/><path d="M16 14l14 8 14-8M30 22v16"/></svg></div>
    <h3>SPECIALIZED LOADS</h3>
    <p>Lorem ipsum dolor sit amet, cons ectetur adipiscing elit, sed do eiu dmod fdsg tempor.</p>
  </div>
  <div class="service" style="left:832px;top:275px">
    <div class="icon"><svg width="54" height="50" viewBox="0 0 54 50" fill="none" stroke="#a50d0d" stroke-width="2"><rect x="10" y="8" width="30" height="26"/><path d="M25 8v26"/><path d="M40 20h6l4 6v8H40"/><circle cx="18" cy="40" r="4"/><circle cx="44" cy="40" r="4"/></svg></div>
    <h3>DRY VANS</h3>
    <p>Lorem ipsum dolor sit amet, cons ectetur adipiscing elit, sed do eiu dmod fdsg tempor.</p>
  </div>
</section>

<!-- ABOUT -->
<section class="section about">
  <div class="photo about-photo" role="img" aria-label="Open highway at dusk"></div>
  <div class="photo about-truck" role="img" aria-label="Red semi truck hauling a white trailer"></div>
  <div class="abs label" style="left:686px;top:72px">LET'S KNOW ABOUT US?</div>
  <h2 class="abs heading" style="left:688px;top:98px">We Transport Logistic<br>For World’s Multinational<br>Companis.</h2>
  <p class="abs para" style="left:688px;top:230px;width:375px">Lorem ipsum dolor sit amet, consectetur adipiscing elit, sed do eiusmod tempor incididunt ut labore et dolore magna aliqua Quis ipsum suspendiss.</p>
  <p class="abs para" style="left:688px;top:319px;width:375px">Lorem ipsum dolor sit amet, consectetur adipiscing elit, sed do eiusmod tempor incididunt.</p>
  <div class="btn" style="left:688px;top:394px;width:140px;height:44px">LEARN MORE</div>
</section>

<!-- TEAM -->
<section class="section team">
  <svg class="abs" style="left:0;top:0" width="1200" height="523" viewBox="0 0 1200 523" aria-hidden="true">
    <polygon points="0,0 440,200 440,330 0,330" fill="#a50d0d"/>
    <polygon points="590,523 1200,280 1200,523" fill="#a50d0d"/>
  </svg>
  <div class="abs label" style="left:0;width:1200px;text-align:center;top:61px">LET'S MEET OUR TEAM</div>
  <h2 class="abs heading" style="left:0;width:1200px;text-align:center;top:92px">Let’s Meet With Our Drivers.</h2>

  <div class="card" style="left:155px"><div class="avatar" role="img" aria-label="Driver portrait"></div><h4>Dorian Pell</h4><p>More modern then the page we have right now. But no ser ious and modern.</p><div class="socials"><span></span><span></span><span></span></div></div>
  <div class="card" style="left:384px"><div class="avatar" role="img" aria-label="Driver portrait"></div><h4>Dorian Pell</h4><p>More modern then the page we have right now. But no ser ious and modern.</p><div class="socials"><span></span><span></span><span></span></div></div>
  <div class="card" style="left:612px"><div class="avatar" role="img" aria-label="Driver portrait"></div><h4>Dorian Pell</h4><p>More modern then the page we have right now. But no ser ious and modern.</p><div class="socials"><span></span><span></span><span></span></div></div>
  <div class="card" style="left:840px"><div class="avatar" role="img" aria-label="Driver portrait"></div><h4>Dorian Pell</h4><p>More modern then the page we have right now. But no ser ious and modern.</p><div class="socials"><span></span><span></span><span></span></div></div>

  <div class="arrow" style="left:96px;top:258px"><svg width="16" height="10" viewBox="0 0 16 10" fill="none" stroke="#a50d0d" stroke-width="2"><path d="M15 5H2M6 1L2 5l4 4"/></svg></div>
  <div class="arrow" style="left:1073px;top:258px;border:1.5px solid #a50d0d"><svg width="16" height="10" viewBox="0 0 16 10" fill="none" stroke="#a50d0d" stroke-width="2"><path d="M1 5h13M10 1l4 4-4 4"/></svg></div>

  <div class="abs dots" style="top:433px"><span class="on"></span><span></span><span></span></div>
</section>

<!-- STATS -->
<section class="section stats">
  <div class="stat" style="left:261px"><strong>300+</strong><span>TRANSPORTED</span></div>
  <div class="stat" style="left:487px"><strong>9000+</strong><span>DISTANCE (MILES)</span></div>
  <div class="stat" style="left:713px"><strong>25+</strong><span>EXPRIENCE (YEAR)</span></div>
  <div class="stat" style="left:931px"><strong>36+</strong><span>SKILED DRIVERS</span></div>
</section>

<!-- QUOTE REQUEST -->
<section class="section quote">
  <svg class="abs" style="left:0;top:0" width="1200" height="603" viewBox="0 0 1200 603" aria-hidden="true">
    <path d="M0 0 C120 180 330 380 715 603 L0 603 Z" fill="#a50d0d"/>
  </svg>
  <div class="photo quote-truck" role="img" aria-label="Red semi truck with white trailer, front three-quarter view"></div>
  <div class="abs label" style="left:611px;top:83px">REQUEST A QUOTE.</div>
  <h2 class="abs heading" style="left:611px;top:108px">Have A Load,Get A Quote!</h2>
  <div class="field-label" style="top:171px">Your Name</div>
  <div class="field" style="top:191px;height:41px">Enter Your Full Name</div>
  <div class="field-label" style="top:254px">Email Address</div>
  <div class="field" style="top:274px;height:40px">Type Your Email Address</div>
  <div class="field-label" style="top:337px">Load Details</div>
  <div class="field area" style="top:358px;height:95px">Pickup, Delivery, Load Type And Weight</div>
  <div class="btn" style="left:611px;top:475px;width:153px;height:45px">GET A QUOTE</div>
</section>

<!-- FOOTER -->
<footer class="section footer">
  <div class="abs foot-brand"><i></i>COPPER LANTERN<br>HAULAGE</div>
  <p class="abs foot-text">Lorem ipsum dolor sit amet, consec tetur adipiscing elit, sed do eiusmod tempor incididunt.</p>
  <div class="abs foot-col" style="left:451px;top:77px"><h5>Queek Links</h5><ul><li>Home</li><li>Security Sales Blog</li><li>Clients</li><li>About</li><li>News</li></ul></div>
  <div class="abs foot-col" style="left:622px;top:77px"><h5>Turms &amp; Conditions</h5><ul><li>Turms Of Company</li><li>Conditions</li><li>Privacy Policy</li><li>Contact Us</li><li>Security Sales</li></ul></div>
  <div class="abs foot-col" style="left:841px;top:77px">
    <h5>CONTACT US</h5>
    <div style="display:flex;align-items:center;gap:14px;font-size:13px">
      <svg width="16" height="16" viewBox="0 0 16 16"><path d="M3 1l3 3-2 2c1 2 3 4 5 5l2-2 3 3-2 3C6 14 2 10 1 3z" fill="#d0202a"/></svg>+1-555-204-7781</div>
    <div style="display:flex;align-items:center;gap:14px;font-size:13px;margin-top:14px">
      <svg width="16" height="12" viewBox="0 0 16 12"><rect width="16" height="12" rx="1" fill="#d0202a"/><path d="M1 1l7 6 7-6" fill="none" stroke="#fff" stroke-width="1.2"/></svg>dispatch@copperlantern.example</div>
    <h5 style="margin-top:22px;margin-bottom:14px">Social Links</h5>
    <div style="display:flex;gap:18px"><div class="ring"></div><div class="ring"></div><div class="ring"></div></div>
  </div>
  <div class="abs rule"></div>
  <div class="abs copy" style="left:157px">@copyright by HALVERSTON 2021, ALL RIGHT RESERVED</div>
  <div class="abs copy" style="left:930px">TURMS &amp; CONDITIONS</div>
</footer>

</body>
</html>
```